Hooded Rogue - Game Company Site

Looking for a simple and sleek 3 page design for a game company site. Will provide a logo to be included in the design. Even though we specialize in flash games at the moment, we plan on expanding to other platforms and would like a site similar to console developer sites than flash game portals. Example: http://brightquill.example

Required Pages:
1. Home: advertising the latest game, big image, and possibly a news post
2. Games: a portfolio of games, each game will have a large image preview and some text, with a link to the game
3. About Us:
A roster of employees, each will have a picture and bio with name, alias, location, and some text.

Would be nice to have a theme inspired by "villains." The logo should provide the general feel we are looking for. You will find the logo attached as a .PSD (Photoshop) and a .PNG to give a quick preview. Vector .ai and .eps logos have also been attached. Feel free to split the text from the character or make any changes you feel necessary!

About Hooded Rogue
We create flash games and are hoping to expand to iPhone games and other platforms in the future!
Our latest game: http://www.plarvexa.example/games/quentloo/tabrin-quest-2-chapter-1

Target Market(s)

18-30 year old male tech and video game enthusiasts

Industry/Entity Type

Advertising

Requirements
Must have
• Must have the logo that is attached.

```html
<!DOCTYPE html>
<html lang="en">
<head>
<meta charset="utf-8">
<title>Hooded Rogue – Game Studio</title>
<link rel="stylesheet" href="https://fonts.googleapis.com/css2?family=Arimo:wght@400;700&family=Libre+Baskerville:ital@1&family=Lilita+One&family=Luckiest+Guy&family=Metamorphous&display=swap">
<style>
:root{
  --navy:#0a3a55;
  --header-blue:#0d5a82;
  --sky:#0c93cf;
  --sky-light:#18a9e4;
  --panel:#050505;
  --card:#1d1d1d;
  --gold:#fbb62a;
  --orange:#f7941d;
  --amber:#e8a32e;
  --white:#fff;
  --footer-ink:#1c4660;
  --display:"Luckiest Guy","Lilita One",sans-serif;
}
*{box-sizing:border-box;margin:0;padding:0}
html,body{width:1200px;height:923px;overflow:hidden}
body{position:relative;font-family:"Arimo",Arial,sans-serif;color:var(--white);
  background:linear-gradient(180deg,var(--sky) 477px,var(--sky-light) 923px)}
a{color:inherit;text-decoration:none}
.site-header{position:absolute;left:0;top:0;width:1200px;height:160px;
  background:radial-gradient(ellipse 420px 260px at 270px 80px,#1676a6 0%,var(--header-blue) 45%,var(--navy) 100%)}
.brand{position:absolute;left:185px;top:58px;display:flex;align-items:center;gap:12px}
.brand-dot{width:40px;height:40px;border-radius:50%;background:var(--gold)}
.brand-name{font-family:var(--display);font-size:30px;color:var(--gold);letter-spacing:1px;text-transform:uppercase}
.follow-top{position:absolute;left:819px;top:0;width:224px;height:53px;background:#06202f;
  display:flex;align-items:center;justify-content:center;gap:10px;border-radius:0 0 3px 3px}
.follow-label{font-family:var(--display);font-size:18px;color:var(--gold);letter-spacing:.5px;text-transform:uppercase;white-space:nowrap}
.social{font-size:11px;font-weight:700;color:var(--white);display:flex;align-items:center;gap:4px}
.social-sq{width:10px;height:10px;background:var(--sky-light)}
.main-nav{position:absolute;top:99px;left:643px;display:flex;gap:16px}
.nav-btn{height:41px;display:flex;align-items:center;justify-content:center;border-radius:3px;
  font-family:var(--display);font-size:19px;letter-spacing:.5px;text-transform:uppercase;
  background:linear-gradient(180deg,#1a9ad4,#0a6b9f);color:#0b4466;border:1px solid #0b5680}
.nav-btn.is-active{background:#0a0a0a;color:var(--orange);border-color:#000}
.nav-home{width:105px}.nav-games{width:117px}.nav-about{width:148px}
.hero{position:absolute;left:0;top:160px;width:1200px;height:317px;
  background:linear-gradient(180deg,#000 0%,#000 40%,#3a2a08 70%,#a8761a 100%);border-bottom:2px solid #0a78ad}
.hero-shot{position:absolute;left:155px;top:18px;width:427px;height:266px;
  background:linear-gradient(180deg,#8c6a54 0%,#a27956 35%,#5e6b2a 60%,#3e4a1c 100%);box-shadow:0 0 6px #000}
.slider-dots{position:absolute;left:337px;top:292px;display:flex;gap:4px}
.slider-dots span{width:10px;height:10px;border-radius:50%;background:#1a1a1a;border:1px solid #6a5020}
.slider-dots span.on{background:var(--gold)}
.hero-copy{position:absolute;left:647px;top:37px;width:410px}
.hero-kicker{font-size:14px;font-weight:700;letter-spacing:-.2px}
.hero-title{font-family:"Metamorphous",serif;font-size:70px;line-height:1;margin-top:4px;
  color:var(--orange);letter-spacing:2px;font-weight:400}
.hero-text{font-size:12.5px;line-height:22px;margin-top:6px;letter-spacing:-.2px}
.hero-actions{position:absolute;left:647px;top:224px;display:flex;gap:17px}
.cta{height:47px;display:flex;align-items:center;justify-content:center;border-radius:3px;
  font-family:var(--display);font-size:24px;color:#2a1a05;letter-spacing:.5px;text-transform:uppercase;
  background:linear-gradient(180deg,#ffc93a,#f7941d)}
.cta-play{width:186px}.cta-learn{width:199px}
.section-title{position:absolute;top:492px;font-family:var(--display);font-size:26px;font-weight:400;
  color:var(--gold);text-shadow:2px 2px 0 #3a2205;transform:translateX(-50%);white-space:nowrap;text-transform:uppercase}
.title-news{left:372px}.title-games{left:824px}
.panel{position:absolute;top:535px;height:288px;background:var(--panel);border-radius:8px}
.news-panel{left:155px;width:436px;padding:20px 18px 0 23px}
.news-item{margin-bottom:16px}
.news-date{font-family:"Libre Baskerville",serif;font-style:italic;font-size:11.5px;color:var(--amber)}
.news-body{font-size:13px;line-height:17px;margin-top:4px;letter-spacing:-.1px}
.games-panel{left:615px;width:435px;padding:10px 12px}
.game-card{position:relative;height:88px;background:var(--card);border-radius:5px;margin-bottom:4px}
.game-thumb{position:absolute;left:6px;top:6px;width:77px;height:77px;border-radius:2px;
  background:linear-gradient(180deg,#ffd23a,#f7a21d);display:flex;align-items:center;justify-content:center}
.game-thumb span{font-family:var(--display);font-size:10px;color:#2a1a05;text-align:center;text-transform:uppercase}
.game-title{position:absolute;left:95px;top:7px;font-size:16.5px;font-weight:700;color:var(--orange)}
.game-text{position:absolute;left:95px;top:31px;width:305px;font-size:13px;line-height:17px}
.more-info{position:absolute;right:12px;bottom:6px;display:flex;align-items:center;gap:8px;
  font-size:10px;font-weight:700;font-style:italic;color:var(--orange)}
.more-info svg{display:block}
.footer-nav{position:absolute;left:155px;top:849px;display:flex;gap:17px;
  font-size:14.5px;font-weight:700;color:var(--footer-ink)}
.footer-info{position:absolute;left:155px;top:869px;font-size:12.5px;color:var(--footer-ink)}
.follow-bottom{position:absolute;left:874px;top:860px;display:flex;align-items:center;gap:10px}
.follow-bottom .follow-label{color:#0b2a3d;font-size:18px}
</style>
</head>
<body>
<header class="site-header">
  <div class="brand"><span class="brand-dot"></span><span class="brand-name">Hooded Rogue</span></div>
  <div class="follow-top">
    <span class="follow-label">Follow us:</span>
    <span class="social"><span class="social-sq"></span>Vellobook</span>
    <span class="social"><span class="social-sq"></span>Skrawlet</span>
  </div>
  <nav class="main-nav">
    <a class="nav-btn nav-home is-active">Home</a>
    <a class="nav-btn nav-games">Games</a>
    <a class="nav-btn nav-about">About us</a>
  </nav>
</header>

<section class="hero">
  <div class="hero-shot" role="img" aria-label="Gameplay screenshot of Tabrin II: two creatures battling in a canyon with health bars and action bar"></div>
  <div class="slider-dots"><span></span><span></span><span class="on"></span><span></span><span></span></div>
  <div class="hero-copy">
    <p class="hero-kicker">FEATURED GAME</p>
    <h1 class="hero-title">TABRIN II</h1>
    <p class="hero-text">Lorem ipsum dolor sit amet, consectetur adipisicing elit, sed do eiusmod tempor incididunt ut labore et dolore magna aliqua. Ut enim ad minimveniam quis nostrud exercitation ullamco laboris nisi ut aliquip ex ea commodoco</p>
  </div>
  <div class="hero-actions">
    <a class="cta cta-play">Play now</a>
    <a class="cta cta-learn">Learn more</a>
  </div>
</section>

<h2 class="section-title title-news">Recent News</h2>
<h2 class="section-title title-games">Featured Games</h2>

<section class="panel news-panel">
  <article class="news-item"><p class="news-date">November 7 2011</p><p class="news-body">Donec sed odio dui. Nulla vitae elit libero, a pharetra augue. Nullam id dolor id nibh ultricies vehicula ut id elit. Integer posuere erat a ante venenatis dapibus posuere velit aliquet.</p></article>
  <article class="news-item"><p class="news-date">November 8 2011</p><p class="news-body">Donec sed odio dui. Nulla vitae elit libero, a pharetra augue. Nullam id dolor id nibh ultricies vehicula ut id elit. Integer posuere erat a ante venenatis dapibus posuere velit aliquet.</p></article>
  <article class="news-item"><p class="news-date">November 9 2011</p><p class="news-body">Donec sed odio dui. Nulla vitae elit libero, a pharetra augue. Nullam id dolor id nibh ultricies vehicula ut id elit. Integer posuere erat a ante venenatis dapibus posuere velit aliquet.</p></article>
</section>

<section class="panel games-panel">
  <article class="game-card">
    <div class="game-thumb"><span>Hooded Rogue</span></div>
    <h3 class="game-title">Featured Game Title</h3>
    <p class="game-text">Donec sed odio dui. Nulla vitae elit libero, a phar etra augue. Nullam id dolor id nibh ultricies vehicula</p>
    <a class="more-info">MORE INFO <svg width="18" height="18" viewBox="0 0 18 18"><circle cx="9" cy="9" r="9" fill="#fbb62a"/><path d="M7 5l5 4-5 4z" fill="#1d1d1d"/></svg></a>
  </article>
  <article class="game-card">
    <div class="game-thumb"><span>Hooded Rogue</span></div>
    <h3 class="game-title">Featured Game Title</h3>
    <p class="game-text">Donec sed odio dui. Nulla vitae elit libero, a phar etra augue. Nullam id dolor id nibh ultricies vehicula</p>
    <a class="more-info">MORE INFO <svg width="18" height="18" viewBox="0 0 18 18"><circle cx="9" cy="9" r="9" fill="#fbb62a"/><path d="M7 5l5 4-5 4z" fill="#1d1d1d"/></svg></a>
  </article>
  <article class="game-card">
    <div class="game-thumb"><span>Hooded Rogue</span></div>
    <h3 class="game-title">Featured Game Title</h3>
    <p class="game-text">Donec sed odio dui. Nulla vitae elit libero, a phar etra augue. Nullam id dolor id nibh ultricies vehicula</p>
    <a class="more-info">MORE INFO <svg width="18" height="18" viewBox="0 0 18 18"><circle cx="9" cy="9" r="9" fill="#fbb62a"/><path d="M7 5l5 4-5 4z" fill="#1d1d1d"/></svg></a>
  </article>
</section>

<footer class="site-footer">
  <nav class="footer-nav"><a>HOME</a><a>GAMES</a><a>ABOUT US</a></nav>
  <p class="footer-info">info@harrowline.example &nbsp;|&nbsp; Call: 555-201-0142| &nbsp;Fax: 555-201-0142 &nbsp;| © All Rights Reserved</p>
  <div class="follow-bottom">
    <span class="follow-label">Follow us:</span>
    <span class="social"><span class="social-sq"></span>Vellobook</span>
    <span class="social"><span class="social-sq"></span>Skrawlet</span>
  </div>
</footer>
</body>
</html>
```